" A LÍVIA TORQUATO é uma empresa do ramo de decoração de casamentos. Há mais de uma década de trabalho, a empresa está passando por um momento de ressignificação do negócio, entre elas a atualização das marcas. No mundo da decoração, as empresas sempre se caracterizam por conceito e estilo. Atualmente a Lívia Torquato tem usado o conceito borró chique e clássico, podendo mudar sempre que houver uma nova tendência ou moda no mundo da decoração. A Lívia Torquato, além de proprietária, é a decoradora master da empresa. Um das principais características identificadas no modelo de atendimento e operações da empresa são: a sofisticação do eventos, comprometimento, responsabilidade, praticidade e solucionadoras de problemas. "

```html
<!DOCTYPE html>
<html lang="pt-BR">
<head>
<meta charset="utf-8">
<title>Lívia Torquato — Papel timbrado</title>
<link href="https://fonts.googleapis.com/css2?family=Montserrat:wght@400;500&family=Great+Vibes&display=swap" rel="stylesheet">
<style>
  :root {
    --backdrop: #ead5d3;
    --paper: #ffffff;
    --rose-gold: #c9948a;
    --rose-soft: #efe2df;
    --ink-muted: #8a8583;
    --band: #e6c6c1;
  }
  * { margin: 0; padding: 0; box-sizing: border-box; }
  html, body {
    width: 1200px; height: 1200px; overflow: hidden;
    background: var(--backdrop);
  }
  .letterhead {
    position: absolute;
    left: 232px; top: 80px;
    width: 736px; height: 1040px;
    background: var(--paper);
    box-shadow: 0 6px 24px rgba(120, 80, 75, 0.12);
    overflow: hidden;
  }
  .brand {
    position: absolute;
    left: 60px; top: 62px;
    text-align: center;
  }
  .brand__name {
    font-family: "Montserrat", sans-serif;
    font-weight: 500;
    font-size: 17px;
    letter-spacing: 2.5px;
    color: var(--rose-gold);
  }
  .brand__tagline {
    margin-top: 4px;
    font-family: "Great Vibes", cursive;
    font-size: 15px;
    color: var(--rose-gold);
  }
  .backdrop-motif {
    position: absolute;
    right: -40px; top: 200px;
    width: 360px; height: 620px;
    border-radius: 48% 40% 45% 50%;
    background: radial-gradient(ellipse at 50% 45%, var(--rose-soft) 0%, rgba(239,226,223,0.35) 55%, rgba(255,255,255,0) 75%);
    opacity: 0.7;
  }
  .contacts {
    position: absolute;
    left: 170px; top: 922px;
    width: 480px;
    display: grid;
    grid-template-columns: 1fr 1fr;
    row-gap: 9px;
    column-gap: 20px;
    font-family: "Montserrat", sans-serif;
    font-size: 9.5px;
    color: var(--ink-muted);
  }
  .contact {
    display: flex; align-items: center; gap: 7px;
    white-space: nowrap;
  }
  .contact svg { width: 12px; height: 12px; flex: none; }
  .footer-band {
    position: absolute;
    left: 40px; right: 40px; bottom: 0;
    height: 14px;
    background: var(--band);
    border-radius: 10px 10px 0 0;
  }
</style>
</head>
<body>
  <main class="letterhead">
    <header class="brand">
      <div class="brand__name">LÍVIA TORQUATO</div>
      <div class="brand__tagline">decoração com amor e estilo</div>
    </header>

    <div class="backdrop-motif" role="img" aria-label="Faint decorative flourish of the brand in soft rose"></div>

    <footer class="contacts">
      <div class="contact">
        <svg viewBox="0 0 12 12" aria-hidden="true"><circle cx="6" cy="6" r="5.2" fill="none" stroke="#8a8583" stroke-width="1"/><path d="M4.2 3.6c.3-.3.7-.3.9 0l.5.8c.2.3.1.6-.1.8l-.3.3c.3.7.8 1.2 1.4 1.5l.3-.3c.2-.2.5-.3.8-.1l.8.5c.3.2.3.6 0 .9-.7.7-1.6.6-2.7-.2-1-.8-1.8-1.8-2-2.7-.1-.6 0-1.1.4-1.5z" fill="#8a8583"/></svg>
        <span>(61) 9 8123-4570</span>
      </div>
      <div class="contact">
        <svg viewBox="0 0 12 12" aria-hidden="true"><rect x="1" y="2.5" width="10" height="7" rx="1" fill="none" stroke="#8a8583" stroke-width="1"/><path d="M1.3 3l4.7 3.6L10.7 3" fill="none" stroke="#8a8583" stroke-width="1"/></svg>
        <span>financeiro@liviatorquato.com.br</span>
      </div>
      <div class="contact">
        <svg viewBox="0 0 12 12" aria-hidden="true"><circle cx="6" cy="6" r="5.2" fill="none" stroke="#8a8583" stroke-width="1"/></svg>
        <span>@liviatorquato.decoracoes</span>
      </div>
      <div class="contact">
        <svg viewBox="0 0 12 12" aria-hidden="true"><circle cx="6" cy="6" r="5.2" fill="none" stroke="#8a8583" stroke-width="1"/><ellipse cx="6" cy="6" rx="2.2" ry="5.2" fill="none" stroke="#8a8583" stroke-width="0.8"/><path d="M0.8 6h10.4" stroke="#8a8583" stroke-width="0.8"/></svg>
        <span>www.liviatorquato.com.br</span>
      </div>
    </footer>

    <div class="footer-band"></div>
  </main>
</body>
</html>
```